Velmorak720 is a marketing advisory service company. We provide the following services:
Marketing Strategy
PR and Marketing Communication
Field Marketing
Digital Marketing

We would like to see a design that has either of the following copy:

Everyone can develop a product for the market; not everyone can access the market with the product. Let Velmorak720 help you access the market profitably.

or

Almost every business know how to create value, nor every business can capture value. At Velmorak720, we specialize in helping businesses capture value.

or

It is easy to start a business, attracting and retaining customers and client is the real work. At Velmorak720, we specialize in helping our businesses attract and retain customers and clients.

We can have a slogan that reads:

V-720, your market development partner.....

```html
<!DOCTYPE html>
<html lang="en">
<head>
<meta charset="utf-8">
<title>Velmorak720 – Display Banner Set</title>
<link rel="stylesheet" href="https://fonts.googleapis.com/css2?family=Open+Sans:wght@400;700&display=swap">
<style>
  :root {
    --brand-blue: #0b4f97;
    --band-blue: #8ea9d8;
    --accent-yellow: #f6ea2a;
    --text-white: #ffffff;
    --page-bg: #ffffff;
  }
  * { box-sizing: border-box; margin: 0; padding: 0; }
  html, body {
    width: 1200px; height: 1000px; overflow: hidden;
    background: var(--page-bg);
    font-family: "Open Sans", Arial, sans-serif;
  }
  .canvas { position: relative; width: 1200px; height: 1000px; }

  .banner {
    position: absolute;
    background: var(--brand-blue);
    overflow: hidden;
    font-weight: 700;
    text-transform: uppercase;
    line-height: 1.25;
  }
  .banner-art { position: absolute; inset: 0; }

  .brand {
    position: absolute;
    display: flex; align-items: center; gap: 6px;
    color: var(--text-white);
    font-weight: 400;
    text-transform: none;
    white-space: nowrap;
    line-height: 1;
  }
  .brand-dot {
    display: inline-block; border-radius: 50%;
    background: var(--accent-yellow);
  }

  .headline { position: absolute; color: var(--text-white); text-align: center; }
  .offer { position: absolute; color: var(--accent-yellow); text-align: center; white-space: nowrap; }
  .offer strong { font-weight: 700; }

  /* Skyscraper 160 x 600 */
  .skyscraper { left: 45px; top: 243px; width: 160px; height: 600px; }
  .skyscraper .brand { left: 6px; top: 102px; font-size: 23px; gap: 4px; }
  .skyscraper .brand-dot { width: 10px; height: 10px; }
  .skyscraper .headline { left: 0; right: 0; top: 141px; font-size: 12.5px; }
  .skyscraper .offer { left: 0; right: 0; top: 478px; font-size: 12.5px; }

  /* Leaderboard 728 x 90 */
  .leaderboard { left: 269px; top: 183px; width: 728px; height: 90px; }
  .leaderboard .brand { left: 12px; top: 52px; font-size: 20px; }
  .leaderboard .brand-dot { width: 9px; height: 9px; }
  .leaderboard .headline { right: 8px; top: 28px; font-size: 12px; line-height: 1.15; }
  .leaderboard .offer { left: 0; right: 0; top: 74px; font-size: 12px; line-height: 1.2; }

  /* Medium rectangles 336 x 280 */
  .rectangle { top: 317px; width: 336px; height: 280px; }
  .rectangle-a { left: 269px; }
  .rectangle-b { left: 629px; }
  .rectangle .brand { left: 4px; top: 81px; font-size: 21px; gap: 5px; }
  .rectangle .brand-dot { width: 10px; height: 10px; }
  .rectangle .headline { left: 110px; right: 0; top: 5px; font-size: 12.5px; }
  .rectangle .offer { left: 0; right: 0; top: 227px; font-size: 12.5px; line-height: 1.35; }

  /* Large rectangle 646 x 220 */
  .large { left: 269px; top: 624px; width: 646px; height: 220px; }
  .large .brand { left: 4px; top: 108px; font-size: 22px; gap: 5px; }
  .large .brand-dot { width: 11px; height: 11px; }
  .large .headline { left: 0; width: 646px; top: 138px; font-size: 14.5px; }
  .large .offer { left: 0; width: 646px; top: 180px; font-size: 14.5px; }
</style>
</head>
<body>
<main class="canvas">

  <!-- Skyscraper -->
  <section class="banner skyscraper">
    <svg class="banner-art" viewBox="0 0 160 600" width="160" height="600">
      <defs>
        <linearGradient id="crowd-tall" x1="0" y1="0" x2="0" y2="1">
          <stop offset="0" stop-color="#e4eef5"/>
          <stop offset="0.35" stop-color="#c7dbe8"/>
          <stop offset="0.55" stop-color="#b85a90"/>
          <stop offset="0.72" stop-color="#3b4f9c"/>
          <stop offset="0.85" stop-color="#d98a4a"/>
          <stop offset="1" stop-color="#e3d8c6"/>
        </linearGradient>
      </defs>
      <path d="M0,252 C50,262 110,262 160,250 L160,268 C110,276 50,274 0,266 Z" fill="#8ea9d8"/>
      <g role="img" aria-label="Painted illustration of a crowd of women in colourful dress carrying baskets on their heads">
        <path d="M0,266 C50,274 110,276 160,266 L160,430 C130,450 70,462 0,466 Z" fill="url(#crowd-tall)"/>
      </g>
      <path d="M0,266 C50,274 110,276 160,266" fill="none" stroke="#f6ea2a" stroke-width="2"/>
      <path d="M0,460 C70,456 130,444 160,426 L160,446 C130,466 70,476 0,480 Z" fill="#8ea9d8"/>
      <path d="M0,462 C70,458 130,446 160,428" fill="none" stroke="#f6ea2a" stroke-width="3"/>
    </svg>
    <div class="brand"><span class="brand-dot"></span>Velmorak720</div>
    <p class="headline">It is easy to start<br>a business,<br>attracting<br>and retaining<br>customers<br>and client<br>is the real work.</p>
    <p class="offer">At Velmorak720,<br>we specialize<br>in helping<br>our businesses<br>attract and retain<br>customers<br>and clients.</p>
  </section>

  <!-- Leaderboard -->
  <section class="banner leaderboard">
    <svg class="banner-art" viewBox="0 0 728 90" width="728" height="90">
      <defs>
        <linearGradient id="crowd-strip" x1="0" y1="0" x2="0" y2="1">
          <stop offset="0" stop-color="#e4eef5"/>
          <stop offset="0.45" stop-color="#b85a90"/>
          <stop offset="0.75" stop-color="#3b4f9c"/>
          <stop offset="1" stop-color="#d98a4a"/>
        </linearGradient>
      </defs>
      <path d="M164,0 C195,36 235,48 300,48 C380,48 430,28 520,19 C600,12 680,10 728,9 L728,3 C680,4 600,6 520,12 C430,20 380,40 300,40 C240,40 205,28 178,0 Z" fill="#8ea9d8"/>
      <g role="img" aria-label="Painted illustration of a colourful crowd carrying baskets">
        <path d="M178,0 L728,0 L728,3 C680,4 600,6 520,12 C430,20 380,40 300,40 C240,40 205,28 178,0 Z" fill="url(#crowd-strip)"/>
      </g>
      <path d="M178,0 C205,28 240,40 300,40 C380,40 430,20 520,12 C600,6 680,4 728,3" fill="none" stroke="#f6ea2a" stroke-width="3"/>
    </svg>
    <div class="brand"><span class="brand-dot"></span>Velmorak720</div>
    <p class="headline">It is easy to start a business,<br>attracting and retaining<br>customers and client is the real work.</p>
    <p class="offer">At Velmorak720, we specialize in helping our businesses attract and retain customers and clients.</p>
  </section>

  <!-- Medium rectangle A -->
  <section class="banner rectangle rectangle-a">
    <svg class="banner-art" viewBox="0 0 336 280" width="336" height="280">
      <defs>
        <linearGradient id="crowd-box-a" x1="0" y1="0" x2="0" y2="1">
          <stop offset="0" stop-color="#e4eef5"/>
          <stop offset="0.3" stop-color="#c7dbe8"/>
          <stop offset="0.5" stop-color="#b85a90"/>
          <stop offset="0.7" stop-color="#3b4f9c"/>
          <stop offset="0.85" stop-color="#d98a4a"/>
          <stop offset="1" stop-color="#e3d8c6"/>
        </linearGradient>
      </defs>
      <path d="M0,116 C80,100 150,118 220,108 C270,100 310,98 336,104 L336,116 C300,110 260,114 220,120 C150,130 80,112 0,128 Z" fill="#8ea9d8"/>
      <g role="img" aria-label="Painted illustration of women in colourful dress walking with baskets on their heads">
        <path d="M0,126 C80,110 150,128 220,118 C270,112 310,110 336,114 L336,176 C300,200 220,212 150,214 C90,216 40,222 0,236 Z" fill="url(#crowd-box-a)"/>
      </g>
      <path d="M0,230 C40,218 90,212 150,210 C220,208 300,196 336,172 L336,186 C300,210 220,222 150,224 C90,226 40,232 0,244 Z" fill="#8ea9d8"/>
      <path d="M0,232 C40,220 90,214 150,212 C220,210 300,198 336,174" fill="none" stroke="#f6ea2a" stroke-width="3"/>
    </svg>
    <div class="brand"><span class="brand-dot"></span>Velmorak720</div>
    <p class="headline">It is easy to start a business,<br>attracting and retaining<br>customers and client<br>is the real work.</p>
    <p class="offer">At <strong>Velmorak720</strong>,<br>we specialize in helping our businesses<br>attract and retain customers and clients.</p>
  </section>

  <!-- Medium rectangle B -->
  <section class="banner rectangle rectangle-b">
    <svg class="banner-art" viewBox="0 0 336 280" width="336" height="280">
      <defs>
        <linearGradient id="crowd-box-b" x1="0" y1="0" x2="0" y2="1">
          <stop offset="0" stop-color="#e4eef5"/>
          <stop offset="0.3" stop-color="#c7dbe8"/>
          <stop offset="0.5" stop-color="#b85a90"/>
          <stop offset="0.7" stop-color="#3b4f9c"/>
          <stop offset="0.85" stop-color="#d98a4a"/>
          <stop offset="1" stop-color="#e3d8c6"/>
        </linearGradient>
      </defs>
      <path d="M0,116 C80,100 150,118 220,108 C270,100 310,98 336,104 L336,116 C300,110 260,114 220,120 C150,130 80,112 0,128 Z" fill="#8ea9d8"/>
      <g role="img" aria-label="Painted illustration of women in colourful dress walking with baskets on their heads">
        <path d="M0,126 C80,110 150,128 220,118 C270,112 310,110 336,114 L336,176 C300,200 220,212 150,214 C90,216 40,222 0,236 Z" fill="url(#crowd-box-b)"/>
      </g>
      <path d="M0,230 C40,218 90,212 150,210 C220,208 300,196 336,172 L336,186 C300,210 220,222 150,224 C90,226 40,232 0,244 Z" fill="#8ea9d8"/>
      <path d="M0,232 C40,220 90,214 150,212 C220,210 300,198 336,174" fill="none" stroke="#f6ea2a" stroke-width="3"/>
    </svg>
    <div class="brand"><span class="brand-dot"></span>Velmorak720</div>
    <p class="headline">It is easy to start a business,<br>attracting and retaining<br>customers and client<br>is the real work.</p>
    <p class="offer">At <strong>Velmorak720</strong>,<br>we specialize in helping our businesses<br>attract and retain customers and clients.</p>
  </section>

  <!-- Large rectangle -->
  <section class="banner large">
    <svg class="banner-art" viewBox="0 0 646 220" width="646" height="220">
      <defs>
        <linearGradient id="crowd-wide" x1="0" y1="0" x2="0" y2="1">
          <stop offset="0" stop-color="#e4eef5"/>
          <stop offset="0.35" stop-color="#c7dbe8"/>
          <stop offset="0.55" stop-color="#b85a90"/>
          <stop offset="0.75" stop-color="#3b4f9c"/>
          <stop offset="0.9" stop-color="#d98a4a"/>
          <stop offset="1" stop-color="#e3d8c6"/>
        </linearGradient>
      </defs>
      <path d="M150,0 C140,50 150,100 190,124 C260,138 420,118 520,120 C580,121 620,130 646,138 L646,118 C610,110 570,104 520,104 C420,104 260,122 200,110 C168,90 160,40 168,0 Z" fill="#8ea9d8"/>
      <g role="img" aria-label="Painted illustration of a crowd of women in colourful dress carrying baskets on their heads">
        <path d="M172,0 L646,0 L646,114 C610,106 570,100 520,100 C420,100 270,118 205,106 C176,88 164,40 172,0 Z" fill="url(#crowd-wide)"/>
      </g>
      <path d="M164,0 C156,44 168,92 200,112 C262,124 420,106 520,106 C570,106 610,112 646,122" fill="none" stroke="#f6ea2a" stroke-width="4"/>
    </svg>
    <div class="brand"><span class="brand-dot"></span>Velmorak720</div>
    <p class="headline">It is easy to start a business,attracting and retaining<br>customers and client is the real work.</p>
    <p class="offer">At Velmorak720, we specialize in helping our businesses<br>attract and retain customers and clients.</p>
  </section>

</main>
</body>
</html>
```